Brelton Services - Fast, Efficient and Gas Mainteance for Domestic, Commercial and Industrial clients

We are in the process of purchasing a new business and would like to get a new logo and business card.
Business is a gas maintenance business that also does new gas installations.
Has been established since 1988.
Services include:
Install all types of gas appliances & equipment inc. hot water units
Maintain / repair / replace all types of gas appliances & equipment

Target Market(s)

Domestic, Commercial and Industrial clients

Industry/Entity Type

Business

Contact Information for Business Card

admin@breltonservices.example.au
07 5382 4690
Brelton Services PTY LTD

Logo Text

Gas Fitting & Plumbing Maintenance Specialists

Font styles to use
Sans Serif

Requirements
Must have
• Logo
• Business name, contact number, email address, web address
• Domestic | Commercial | Industrial Est Since 1988
Nice to have
• Possibly a black card with a flame logo to one side
Should not have
• Spelling errors

```html
<!DOCTYPE html>
<html lang="en">
<head>
<meta charset="utf-8">
<title>Brelton Services – Business Card</title>
<link rel="stylesheet" href="https://fonts.googleapis.com/css2?family=Arimo:wght@400;700&family=Open+Sans:wght@400&display=swap">
<style>
  :root {
    --backdrop: #d6c09a;
    --card: #000000;
    --brand-blue: #0a9ee0;
    --text-light: #f2f2f2;
    --text-muted: #b8b8b8;
    --tab-grey: #c4c4c4;
    --icon-dark: #111111;
  }
  html, body {
    margin: 0;
    padding: 0;
    width: 1200px;
    height: 1200px;
    overflow: hidden;
    background: var(--backdrop);
  }
  .canvas {
    position: relative;
    width: 1200px;
    height: 1200px;
    font-family: "Arimo", Arial, sans-serif;
  }
  .card {
    position: absolute;
    left: 196px;
    width: 872px;
    height: 485px;
    background: var(--card);
    border-radius: 32px;
    overflow: hidden;
  }
  .card--front { top: 88px; }
  .card--back { top: 658px; }

  .wordmark {
    font-family: "Arimo", Arial, sans-serif;
    font-weight: 700;
    color: var(--brand-blue);
    letter-spacing: 1px;
    line-height: 1;
    white-space: nowrap;
  }
  .card--front .wordmark {
    position: absolute;
    left: 0;
    right: 0;
    top: 200px;
    text-align: center;
    font-size: 84px;
  }
  .brand-block {
    position: absolute;
    left: 97px;
    top: 166px;
    width: 246px;
  }
  .brand-block .wordmark {
    font-size: 50px;
    text-align: left;
  }
  .company-name {
    margin-top: 18px;
    font-size: 19px;
    color: var(--text-light);
    letter-spacing: 0.5px;
    white-space: nowrap;
  }
  .tagline {
    margin-top: 18px;
    font-family: "Open Sans", Arial, sans-serif;
    font-size: 10.5px;
    color: var(--text-muted);
    white-space: nowrap;
  }
  .contact-list {
    position: absolute;
    right: 86px;
    top: 144px;
    margin: 0;
    padding: 0;
    list-style: none;
    text-align: right;
  }
  .contact-list li {
    height: 53px;
    font-size: 21px;
    color: var(--text-light);
    letter-spacing: 0.4px;
    white-space: nowrap;
  }
  .contact-list li.contact-address { word-spacing: 4px; }
  .contact-list li.contact-phone { word-spacing: 6px; }
  .icon-tab {
    position: absolute;
    right: 0;
    top: 84px;
    width: 68px;
    height: 314px;
    background: var(--tab-grey);
    border-radius: 18px 0 0 18px;
  }
  .icon-tab .icon {
    position: absolute;
    left: 6px;
    width: 24px;
    height: 24px;
  }
  .icon-tab .divider {
    position: absolute;
    left: 0;
    width: 46px;
    height: 1.5px;
    background: var(--icon-dark);
  }
</style>
</head>
<body>
<div class="canvas">
  <section class="card card--front" aria-label="Card front">
    <div class="wordmark">BRELTON</div>
  </section>

  <section class="card card--back" aria-label="Card back">
    <div class="brand-block">
      <div class="wordmark">BRELTON</div>
      <div class="company-name">Brelton Services PTY LTD</div>
      <div class="tagline">Domestic | Commercial | Industrial Est Since 1988</div>
    </div>

    <ul class="contact-list">
      <li class="contact-address">Address 01, Address, City.</li>
      <li class="contact-phone">07 5382 4690</li>
      <li class="contact-email">admin@breltonservices.example.au</li>
      <li class="contact-web">www.breltonservices.example.au</li>
    </ul>

    <div class="icon-tab">
      <svg class="icon" style="top:61px" viewBox="0 0 24 24" aria-hidden="true">
        <path d="M12 3 L2 12 L5 12 L5 21 L10 21 L10 15 L14 15 L14 21 L19 21 L19 12 L22 12 Z" fill="var(--icon-dark)"/>
      </svg>
      <div class="divider" style="top:96px"></div>
      <svg class="icon" style="top:115px" viewBox="0 0 24 24" aria-hidden="true">
        <path d="M6.6 2.5 L9.5 6.8 L7.6 9 C8.6 12 11.5 15.2 14.6 16.5 L16.8 14.5 L21 17.5 L19 21 C11 21 3 13 3.2 4.6 Z" fill="var(--icon-dark)"/>
      </svg>
      <div class="divider" style="top:151px"></div>
      <svg class="icon" style="top:169px" viewBox="0 0 24 24" aria-hidden="true">
        <circle cx="12" cy="12" r="4" fill="none" stroke="var(--icon-dark)" stroke-width="2.4"/>
        <path d="M16 8 L16 14 C16 16.5 20 16.5 20.5 13 C21.5 7 17 2.5 12 2.5 C6.5 2.5 2.5 6.8 2.5 12 C2.5 17.5 7 21.5 12 21.5 C14 21.5 15.5 21 17 20" fill="none" stroke="var(--icon-dark)" stroke-width="2.4"/>
      </svg>
      <div class="divider" style="top:206px"></div>
      <svg class="icon" style="top:222px" viewBox="0 0 24 24" aria-hidden="true">
        <g fill="none" stroke="var(--icon-dark)" stroke-width="1.8">
          <circle cx="12" cy="12" r="9.5"/>
          <ellipse cx="12" cy="12" rx="4.2" ry="9.5"/>
          <line x1="2.5" y1="12" x2="21.5" y2="12"/>
          <path d="M4.2 7 H19.8 M4.2 17 H19.8"/>
        </g>
      </svg>
      <div class="divider" style="top:260px"></div>
    </div>
  </section>
</div>
</body>
</html>
```